'Tarovin' a financial/crypto-currency exchange in the middle east

On the card we need 1) Name 2) title 3) email address 4) phone number using the same colors and theme as the logo. On one side we just want the logo and we want the whole card to be in blue (same blue as logo) with the logo in the back being white.
Industry/Entity Type
Financial

```html
<!DOCTYPE html>
<html lang="en">
<head>
<meta charset="utf-8">
<title>Tarovin business card</title>
<link rel="stylesheet" href="https://fonts.googleapis.com/css2?family=Roboto:wght@400;500&display=swap">
<style>
  :root {
    --brand-blue: #1690cf;
    --card-white: #f2f2f2;
    --backdrop: #2b2b2b;
    --ink-white: #ffffff;
  }
  * { margin: 0; padding: 0; box-sizing: border-box; }
  html, body { width: 1200px; height: 960px; overflow: hidden; }
  body {
    position: relative;
    background: var(--backdrop);
    font-family: "Roboto", sans-serif;
  }
  .card {
    position: absolute;
    left: 320px;
    width: 600px;
    height: 342px;
    border-radius: 22px;
    overflow: hidden;
  }
  .card-front {
    top: 108px;
    background: var(--brand-blue);
    color: var(--ink-white);
  }
  .front-wordmark {
    position: absolute;
    left: 0; right: 0;
    top: 118px;
    text-align: center;
    font-size: 68px;
    font-weight: 500;
    line-height: 1;
    color: var(--ink-white);
  }
  .front-website {
    position: absolute;
    left: 0; right: 0;
    top: 297px;
    text-align: center;
    font-size: 14px;
    letter-spacing: 6px;
    color: var(--ink-white);
  }
  .card-back {
    top: 493px;
    background: var(--card-white);
  }
  .back-swoosh {
    position: absolute;
    inset: 0;
    width: 600px;
    height: 342px;
  }
  .brand-lockup {
    position: absolute;
    left: 48px;
    top: 70px;
    display: flex;
    align-items: center;
    gap: 15px;
  }
  .brand-dot {
    width: 80px;
    height: 80px;
    border-radius: 50%;
    border: 4px solid var(--brand-blue);
  }
  .brand-name {
    font-size: 44px;
    font-weight: 500;
    color: var(--brand-blue);
    line-height: 1;
  }
  .contact-block {
    position: absolute;
    right: 22px;
    top: 213px;
    text-align: right;
    color: var(--ink-white);
  }
  .person-name {
    font-size: 22px;
    font-weight: 500;
    line-height: 1.1;
  }
  .person-title {
    font-size: 15px;
    font-weight: 400;
    margin-top: 3px;
    margin-bottom: 14px;
  }
  .contact-line {
    display: flex;
    justify-content: flex-end;
    align-items: center;
    gap: 8px;
    font-size: 14px;
    line-height: 19px;
  }
  .contact-icon {
    width: 13px;
    height: 13px;
    flex: none;
  }
</style>
</head>
<body>

  <section class="card card-front">
    <div class="front-wordmark">Tarovin</div>
    <div class="front-website">www.tarovin.com</div>
  </section>

  <section class="card card-back">
    <svg class="back-swoosh" viewBox="0 0 600 342" aria-hidden="true">
      <path d="M0 272 C210 300 460 250 600 8 L600 342 L0 342 Z" fill="var(--brand-blue)"/>
      <path d="M0 278 C200 300 420 262 520 140" fill="none" stroke="var(--ink-white)" stroke-width="3"/>
      <path d="M0 264 C220 296 430 250 510 130" fill="none" stroke="var(--brand-blue)" stroke-width="2"/>
    </svg>

    <div class="brand-lockup">
      <div class="brand-dot"></div>
      <div class="brand-name">Tarovin</div>
    </div>

    <div class="contact-block">
      <div class="person-name">DANIEL HARLOW</div>
      <div class="person-title">CEO/FOUNDER</div>
      <div class="contact-line">
        <span>614 208 3917</span>
        <svg class="contact-icon" viewBox="0 0 16 16" aria-hidden="true">
          <path d="M3.5 1 L6 1 L7 5 L5.2 6.3 C6 8 7.8 9.9 9.7 10.8 L11 9 L15 10 L15 12.5 C15 13.9 13.9 15 12.5 15 C6.7 15 1 9.3 1 3.5 C1 2.1 2.1 1 3.5 1 Z" fill="var(--ink-white)"/>
        </svg>
      </div>
      <div class="contact-line">
        <span>daniel@tarovin.com</span>
        <svg class="contact-icon" viewBox="0 0 16 16" aria-hidden="true">
          <rect x="1" y="3" width="14" height="10" fill="var(--ink-white)"/>
          <path d="M1 3 L8 9 L15 3" fill="none" stroke="var(--brand-blue)" stroke-width="1.2"/>
        </svg>
      </div>
      <div class="contact-line">
        <span>www.tarovin.com</span>
        <svg class="contact-icon" viewBox="0 0 16 16" aria-hidden="true">
          <circle cx="8" cy="8" r="7" fill="var(--ink-white)"/>
          <ellipse cx="8" cy="8" rx="3" ry="7" fill="none" stroke="var(--brand-blue)" stroke-width="1"/>
          <line x1="1" y1="8" x2="15" y2="8" stroke="var(--brand-blue)" stroke-width="1"/>
        </svg>
      </div>
    </div>
  </section>

</body>
</html>
```